Business Card Design for digital storytelling business

I need a business card for a workshop/consulting/coaching business.

Company Name: The Bright Harbor

Tagline: New ways to keep old memories

What we do: Through workshops, webinars, and coaching we teach you how to capture, tell and share your important memories and stories using readily available digital tools. We will help you tell your life story in a format to share with your family now and in the future.
Updates

I just received a toll free number that I would like included on the designs. If the addition of a phone number would significantly alter your design, please submit an altered version. The number is 877-512-6098

Target Market(s)

Adults in US between ages of 35-70 interested in capturing, preserving and sharing memories and life stories in a digital format.
Could include the following:

-People touched by illness or tragedy who need to tell their own or a loved one's life story
-Grandparents wanting to share stories and wisdom with grandchildren living far away
-People with aging parents who want to capture their stories in a format to pass on to their children
-Alzheimer's patients and their families
-People wanting to transfer analog photos to digital; or wanting to organize digital photos into something that tells a story

Industry/Entity Type

Digital

Requirements
Must have
• Must include business name, logo, tagline

Contact information (see file)
Social media information

Fonts easily readable by aging eyes. Good contrast.

Nice to have
• Color preferences: blue, green, yellow/gold
Blue denotes the calm, non-pressured way that I teach. It is for the healing that comes from telling your story. It represents time and space that are bridged in the digital environment.
Green is for growth, the future, the family tree, Vines that grow and branch and connect the generations and our hearts.
Yellow/gold is for the legacy of wisdom in our lives and stories. It is for the light of truth we bring to the world by sharing our stories.
Should not have
• No old-style, script fonts.
No Times New Roman

```html
<!DOCTYPE html>
<html lang="en">
<head>
<meta charset="utf-8">
<title>The Bright Harbor — Business Card</title>
<link rel="stylesheet" href="https://fonts.googleapis.com/css2?family=Ubuntu:wght@400;500&family=Montserrat:wght@500&display=swap">
<style>
  :root {
    --navy: #33446e;
    --cream: #ecd9a8;
    --green: #1f9a4a;
    --white: #ffffff;
    --ink: #2a2f3d;
    --backdrop: #ecebe8;
  }
  * { margin: 0; padding: 0; box-sizing: border-box; }
  html, body { width: 1200px; height: 828px; overflow: hidden; }
  body {
    background: var(--backdrop);
    font-family: "Ubuntu", sans-serif;
    display: flex;
    align-items: center;
    justify-content: center;
    gap: 40px;
  }
  .card {
    position: relative;
    width: 560px;
    height: 320px;
    overflow: hidden;
    box-shadow: 0 6px 18px rgba(0,0,0,.18);
  }
  .card-shape { position: absolute; inset: 0; width: 100%; height: 100%; }

  /* front */
  .front-brand {
    position: absolute;
    left: 60px;
    top: 92px;
    display: flex;
    align-items: center;
    gap: 16px;
  }
  .brand-dot {
    flex: none;
    width: 44px; height: 44px;
    border-radius: 50%;
    border: 2px solid var(--white);
  }
  .brand-name {
    font-size: 32px;
    font-weight: 500;
    color: var(--white);
    line-height: 1;
    white-space: nowrap;
  }
  .brand-tagline {
    margin-top: 6px;
    font-family: "Montserrat", sans-serif;
    font-size: 10px;
    letter-spacing: .08em;
    text-transform: uppercase;
    color: var(--white);
    white-space: nowrap;
  }
  .front-web {
    position: absolute;
    left: 0; right: 0;
    bottom: 42px;
    text-align: center;
    font-size: 18px;
    letter-spacing: .32em;
    color: var(--ink);
  }

  /* back */
  .back-brand {
    position: absolute;
    left: 34px;
    bottom: 46px;
    display: flex;
    align-items: center;
    gap: 12px;
  }
  .back-brand .brand-dot { width: 34px; height: 34px; border-color: var(--navy); }
  .back-brand .brand-name { font-size: 26px; color: var(--navy); }
  .back-brand .brand-tagline { color: var(--navy); font-size: 9px; }

  .contact {
    position: absolute;
    right: 26px;
    top: 26px;
    text-align: right;
    color: var(--white);
  }
  .person-name {
    font-size: 18px;
    font-weight: 500;
    letter-spacing: .08em;
    text-transform: uppercase;
  }
  .person-role { font-size: 12px; margin-top: 3px; }
  .address { margin-top: 26px; font-size: 12px; line-height: 1.45; }
  .contact-list { list-style: none; margin-top: 20px; font-size: 12px; }
  .contact-list li {
    display: flex;
    justify-content: flex-end;
    align-items: center;
    gap: 8px;
    line-height: 22px;
  }
  .icon { width: 13px; height: 13px; fill: none; stroke: var(--white); stroke-width: 1.6; }
</style>
</head>
<body>

  <section class="card card-front" aria-label="Card front">
    <svg class="card-shape" viewBox="0 0 560 320" preserveAspectRatio="none" aria-hidden="true">
      <rect width="560" height="320" fill="var(--navy)"/>
      <path d="M0,236 C210,252 430,175 560,18 L560,320 L0,320 Z" fill="var(--cream)"/>
      <path d="M0,236 C210,252 430,175 560,18" fill="none" stroke="var(--green)" stroke-width="9"/>
    </svg>
    <div class="front-brand">
      <span class="brand-dot"></span>
      <div>
        <div class="brand-name">The Bright Harbor</div>
        <div class="brand-tagline">New ways to keep old memories</div>
      </div>
    </div>
    <p class="front-web">www.brightharbor.com</p>
  </section>

  <section class="card card-back" aria-label="Card back">
    <svg class="card-shape" viewBox="0 0 560 320" preserveAspectRatio="none" aria-hidden="true">
      <rect width="560" height="320" fill="var(--navy)"/>
      <path d="M0,112 C240,104 390,200 402,320 L0,320 Z" fill="var(--cream)"/>
      <path d="M0,112 C240,104 390,200 402,320" fill="none" stroke="var(--green)" stroke-width="9"/>
    </svg>
    <div class="back-brand">
      <span class="brand-dot"></span>
      <div>
        <div class="brand-name">The Bright Harbor</div>
        <div class="brand-tagline">New ways to keep old memories</div>
      </div>
    </div>
    <div class="contact">
      <div class="person-name">Owen Marlowe</div>
      <div class="person-role">Managing Director</div>
      <p class="address">214 Harbor Street<br>Lakeview OR</p>
      <ul class="contact-list">
        <li>503-555-0110
          <svg class="icon" viewBox="0 0 16 16" aria-hidden="true"><path d="M3 2l3 1 1 3-2 1c1 2 2 3 4 4l1-2 3 1 1 3-2 1C7 14 2 9 2 4z"/></svg>
        </li>
        <li>503-555-0142
          <svg class="icon" viewBox="0 0 16 16" aria-hidden="true"><rect x="4" y="1.5" width="8" height="13" rx="1.5"/><path d="M7 12h2"/></svg>
        </li>
        <li>503-555-0187
          <svg class="icon" viewBox="0 0 16 16" aria-hidden="true"><rect x="2" y="6" width="12" height="8"/><path d="M5 6V2h6v4M5 10h6"/></svg>
        </li>
        <li>hello@brightharbor.com
          <svg class="icon" viewBox="0 0 16 16" aria-hidden="true"><rect x="1.5" y="3.5" width="13" height="9"/><path d="M1.5 3.5l6.5 5 6.5-5"/></svg>
        </li>
        <li>www.brightharbor.com
          <svg class="icon" viewBox="0 0 16 16" aria-hidden="true"><circle cx="8" cy="8" r="6.3"/><path d="M1.7 8h12.6M8 1.7c-3 3.5-3 9 0 12.6M8 1.7c3 3.5 3 9 0 12.6"/></svg>
        </li>
      </ul>
    </div>
  </section>

</body>
</html>
```